Lorna Tess Tresses Fancy Business Card’s

I want my business cards to be elite, original and very classy. I want the business cards to match the colors of my logo and to match the design posted. I would love the design of the picture I posted

I want the card all white .
The dripping on the top of the card I want it to match the pink color in my logo that’s also posted .
I need my logo on the business card !
I need my Instagram- @lorna.tess.tresses__
And my phone number - 582 907 3365

Target Market(s)

My target market is young woman age 23 to older woman to the age of 65
I want both older and younger women to love my design . I don’t want any cheap looking business cards

Industry/Entity Type

Hair And Beauty

Contact Information for Business Card

Add my logo
Add my Instagram- @lorna.tess.tresses__
My number - 582 907 3365
My website- www.lornatesstresses.example

Font styles to use
Serif
Script

Colors
ffffff
e667a6
e34298

Requirements
Must have
• The business cards must have my logo, my number , my website, and my Instagram!
Nice to have
• Nice to have glitter words that match my logo
• The business cards must look classy and mature
• I want them to be very unique!!
Should not have
• Should not have any colors that doesn’t match my logo ! This is very important! Please

```html
<!DOCTYPE html>
<html lang="en">
<head>
<meta charset="utf-8">
<title>Lorna Tess Tresses — Business Card</title>
<link rel="stylesheet" href="https://fonts.googleapis.com/css2?family=Montserrat:wght@300;400&family=Playfair+Display:wght@600;700&display=swap">
<style>
  :root {
    --white: #ffffff;
    --pink: #e34298;
    --pink-soft: #e667a6;
    --silver: #a9a9ab;
    --silver-dark: #8a8a8d;
    --page: #ffffff;
    --edge: #e6e6e8;
  }
  * { margin: 0; padding: 0; box-sizing: border-box; }
  html, body {
    width: 1200px; height: 1197px; overflow: hidden;
    background: var(--page);
  }
  .sheet { position: relative; width: 1200px; height: 1197px; }

  .card {
    position: absolute; left: 253px; width: 694px; height: 396px;
    background: var(--white); border: 1px solid var(--edge); overflow: hidden;
  }
  .card--front { top: 108px; }
  .card--back { top: 651px; }

  /* front */
  .drip-band {
    position: absolute; left: 0; top: 0; width: 100%; height: 140px;
    background: linear-gradient(to bottom, var(--pink) 0%, var(--pink) 45%, var(--pink-soft) 75%, rgba(230,103,166,0) 100%);
  }
  .brand {
    position: absolute; left: 0; right: 0; top: 190px; text-align: center;
    font-family: "Playfair Display", Georgia, serif; font-weight: 700;
    font-size: 46px; color: var(--pink); letter-spacing: 1px; line-height: 1.1;
  }
  .website {
    position: absolute; left: 0; right: 0; top: 358px; text-align: center;
    font-family: "Montserrat", Arial, sans-serif; font-weight: 400;
    font-size: 18px; letter-spacing: 4px; color: var(--pink);
  }

  /* back */
  .texture-fill {
    position: absolute; inset: 0;
    background: linear-gradient(135deg, var(--silver) 0%, var(--silver-dark) 50%, var(--silver) 100%);
  }
  .frame-outer {
    position: absolute; left: 27px; top: 82px; width: 639px; height: 233px;
    background: var(--white);
  }
  .frame-texture {
    position: absolute; left: 12px; top: 14px; right: 12px; bottom: 14px;
    background: linear-gradient(135deg, var(--silver) 0%, var(--silver-dark) 50%, var(--silver) 100%);
  }
  .frame-inner {
    position: absolute; left: 29px; top: 28px; width: 584px; height: 176px;
    background: var(--white);
  }
  .mini-brand {
    position: absolute; left: 12px; top: 18px; width: 70px;
    font-family: "Playfair Display", Georgia, serif; font-weight: 700;
    font-size: 10px; line-height: 1.15; color: var(--pink); text-align: center;
  }
  .icon-bar {
    position: absolute; left: 83px; top: 51px; width: 33px; height: 125px;
    background: var(--pink);
  }
  .icon-bar svg { position: absolute; left: 8px; width: 17px; height: 17px; }
  .icon-bar .icon-phone { top: 6px; }
  .icon-bar .icon-social { top: 50px; }
  .contact {
    position: absolute; font-family: "Playfair Display", Georgia, serif;
    font-weight: 700; font-size: 29px; color: var(--pink); letter-spacing: 3px;
    white-space: nowrap;
  }
  .contact--phone { left: 182px; top: 44px; }
  .contact--handle { left: 148px; top: 88px; font-size: 27px; }
</style>
</head>
<body>
<div class="sheet">
  <section class="card card--front">
    <div class="drip-band" role="img" aria-label="Pink dripping paint border along the top edge"></div>
    <div class="brand">Lorna Tess<br>Tresses</div>
    <div class="website">www.lornatesstresses.example</div>
  </section>

  <section class="card card--back">
    <div class="texture-fill" role="img" aria-label="Silver glitter texture background"></div>
    <div class="frame-outer">
      <div class="frame-texture" role="img" aria-label="Silver glitter frame"></div>
      <div class="frame-inner">
        <div class="mini-brand">Lorna Tess Tresses</div>
        <div class="icon-bar">
          <svg class="icon-phone" viewBox="0 0 24 24" aria-hidden="true">
            <path fill="#ffffff" d="M6.6 10.8a15.1 15.1 0 0 0 6.6 6.6l2.2-2.2c.3-.3.7-.4 1-.2 1.1.4 2.3.6 3.6.6.6 0 1 .4 1 1V20c0 .6-.4 1-1 1A17 17 0 0 1 3 4c0-.6.4-1 1-1h3.5c.6 0 1 .4 1 1 0 1.3.2 2.5.6 3.6.1.3 0 .7-.2 1z"/>
          </svg>
          <svg class="icon-social" viewBox="0 0 24 24" aria-hidden="true">
            <rect x="3" y="3" width="18" height="18" rx="2" fill="none" stroke="#ffffff" stroke-width="2.2"/>
          </svg>
        </div>
        <div class="contact contact--phone">582 907 3365</div>
        <div class="contact contact--handle">@lorna.tess.tresses__</div>
      </div>
    </div>
  </section>
</div>
</body>
</html>
```